Business card and Stationery for data intelligence company

We need a new design for our business cards and stationery (Business Letter templates and a Quote example on Word, but it MUST work on Google Doc as well).

We are a software company based in Ireland and UK. Our product is "Quarla", data intelligence platform with beautiful visualizations, graph capabilities (things are interconnected), powerful, flexible, it can manage Big Data and Streaming information. It's modern and relatively open source.
Our company will provide data intelligence for law enforcements, pharmaceuticals, and similar high end customers.

We'll launch a new website soon. At the moment it's http://www.quarla.tech if you want to take a look. This is our youtube channel in case you need it to understand what Quarla is: https://www.youtube.com/c/quarlatechchannel

We changed the logo so please use the logo I attach here.

We'd like the output to be cool and modern but elegant and "business" at the same time. It should inspire simple sophistication, "unity" "intent" "purpose" yet subtly very advanced and innovative.

The name "Quarla" does NOT refer to sirens (mithological creatures) as well as the warning devices. It means Quantum Unified Archival Record Layer Array. Please use our logo's colors and if you want to something like the "graph" image.

```html
<!DOCTYPE html>
<html lang="en">
<head>
<meta charset="utf-8">
<title>Quarla — Business Card</title>
<link rel="stylesheet" href="https://fonts.googleapis.com/css2?family=Questrial&display=swap">
<style>
  :root {
    --backdrop: #e6e6e6;
    --card-dark: #242424;
    --card-light: #efefef;
    --brand-amber: #f0a630;
    --ink: #2e2e2e;
    --muted-grey: #bdbdbd;
  }
  * { box-sizing: border-box; margin: 0; padding: 0; }
  html, body {
    width: 1200px; height: 800px; overflow: hidden;
    background: var(--backdrop);
    font-family: "Questrial", "Century Gothic", sans-serif;
  }
  .canvas { position: relative; width: 1200px; height: 800px; }

  .card {
    position: absolute;
    width: 480px; height: 312px;
    left: 376px;
    box-shadow: 0 2px 6px rgba(0,0,0,0.12);
    overflow: hidden;
  }
  .card--front { top: 70px; background: var(--card-dark); }
  .card--back  { top: 414px; background: var(--card-light); }

  .wordmark {
    position: absolute;
    display: flex; align-items: center;
  }
  .wordmark__dot {
    border-radius: 50%;
    border-style: solid;
    border-color: var(--brand-amber);
  }
  .wordmark__name {
    color: var(--brand-amber);
    text-transform: uppercase;
    line-height: 1;
  }
  .card--front .wordmark { left: 92px; top: 112px; }
  .card--front .wordmark__dot { width: 80px; height: 80px; border-width: 8px; margin-right: 22px; }
  .card--front .wordmark__name { font-size: 50px; letter-spacing: 7px; }

  .card--back .wordmark { left: 16px; top: 64px; }
  .card--back .wordmark__dot { width: 48px; height: 48px; border-width: 5px; margin-right: 14px; }
  .card--back .wordmark__name { font-size: 30px; letter-spacing: 4px; }

  .network-graphic {
    position: absolute; left: 224px; top: 0;
    width: 258px; height: 148px;
    background: radial-gradient(ellipse at 70% 35%, rgba(240,166,48,0.35), rgba(189,189,189,0.28) 55%, rgba(239,239,239,0) 80%);
  }

  .employee {
    position: absolute; left: 0; top: 154px;
    display: flex; align-items: stretch;
  }
  .employee__bar { width: 14px; height: 37px; background: var(--brand-amber); border-radius: 0 3px 3px 0; }
  .employee__text { margin-left: 15px; color: var(--brand-amber); font-size: 15px; line-height: 18px; }
  .employee__name { text-transform: uppercase; }

  .contact-list {
    position: absolute; left: 28px; top: 211px;
    list-style: none; color: var(--ink);
    font-size: 15px; line-height: 17.5px;
  }
  .contact-list li { display: flex; align-items: center; }
  .contact-list svg { width: 11px; height: 11px; margin-right: 6px; fill: var(--brand-amber); }

  .address {
    position: absolute; right: 22px; top: 246px;
    color: var(--ink); font-size: 13px; line-height: 16px;
  }
</style>
</head>
<body>
<main class="canvas">
  <section class="card card--front">
    <div class="wordmark">
      <span class="wordmark__dot"></span>
      <span class="wordmark__name">Quarla</span>
    </div>
  </section>

  <section class="card card--back">
    <div class="network-graphic" role="img" aria-label="Connected network of amber and grey hexagon nodes"></div>

    <div class="wordmark">
      <span class="wordmark__dot"></span>
      <span class="wordmark__name">Quarla</span>
    </div>

    <div class="employee">
      <div class="employee__bar"></div>
      <div class="employee__text">
        <div class="employee__name">Employee Name</div>
        <div class="employee__title">Title</div>
      </div>
    </div>

    <ul class="contact-list">
      <li><svg viewBox="0 0 12 12" aria-hidden="true"><rect x="1" y="0" width="10" height="12" rx="2"/><rect x="3" y="2" width="6" height="7" fill="#efefef"/></svg>800.444.6161</li>
      <li><svg viewBox="0 0 12 12" aria-hidden="true"><rect x="3" y="0" width="6" height="3"/><rect x="0" y="4" width="12" height="5" rx="1"/><rect x="3" y="8" width="6" height="4"/></svg>800.444.7272</li>
      <li><svg viewBox="0 0 12 12" aria-hidden="true"><rect x="0" y="2" width="12" height="8"/><path d="M0 2 L6 7 L12 2" stroke="#efefef" stroke-width="1.2" fill="none"/></svg>info@quarla.tech</li>
      <li><svg viewBox="0 0 12 12" aria-hidden="true"><circle cx="6" cy="6" r="5.5"/><path d="M0.5 6 H11.5 M6 0.5 V11.5" stroke="#efefef" stroke-width="1"/></svg>www.quarla.tech</li>
    </ul>

    <address class="address" style="font-style: normal;">
      42 Harbour Row Suite 210,<br>Dublin IE D02 X7K9
    </address>
  </section>
</main>
</body>
</html>
```